Stationary pack for BrightNest

BrightNest is a recently establish Solar brokerage company based in Australia. We have a number of sales staff who provide advice and guidance to both residential and commercial customers regarding solar systems (solar hot water and solar panels.)

In addition to our brokerage services we are also developing software for the solar industry, which will be used to automate the solar system install process. This system will be used by other companies in the solar industry including installers, wholesalers and government departments.

We are after a stationary pack that consists of the following: Business cards, compliments slip and letter head.

The EPS, AI, PNG etc files for the logo are attached.

For the business card:
The name and logo of the company need to be clearly visible. On the back of the business cards, we would like the logo. I am happy for you to split the image part of the logo from the text if you think it would look better a different way.

I would like the business cards to be easily readable with the following information on the front:
Name
(Please leave room for titles for the future – eg Sales Advisor.)
Mobile
Office
Email
Address
ABN

Letter heads:
I would prefer the address to be at the top

Compliments slips:
Only need to be one sided

Target Market(s)

BrightNest provides services to both residential and commercial customers. Our customers will be environmentally conscious.

Industry/Entity Type

Residential

Requirements
Must have
• Business cards must have the logo on the back.

```html
<!DOCTYPE html>
<html lang="en">
<head>
<meta charset="utf-8">
<title>BrightNest Business Cards</title>
<link href="https://fonts.googleapis.com/css2?family=Arimo:ital,wght@0,400;0,700;1,700&display=swap" rel="stylesheet">
<style>
  :root {
    --sheet: #d4dbdb;
    --card: #ffffff;
    --leaf: #6fc51d;
    --leaf-dark: #4ea010;
    --band-top: #f2f23a;
    --band-bottom: #fbe23a;
    --sun: #f7b21c;
    --sun-light: #fde06a;
    --sun-edge: #e8901a;
  }
  * { margin: 0; padding: 0; box-sizing: border-box; }
  html, body { width: 928px; height: 1200px; overflow: hidden; }
  body { background: var(--sheet); font-family: "Arimo", Arial, sans-serif; position: relative; }

  .card { position: absolute; width: 380px; height: 218px; background: var(--card); overflow: hidden; }
  .card--back { left: 54px; }
  .card--front { left: 485px; }

  .brand { position: absolute; inset: 0; display: flex; flex-direction: column; align-items: center; justify-content: center; gap: 14px; }
  .brand__dot { width: 54px; height: 54px; border-radius: 50%;
    background: radial-gradient(circle at 40% 35%, var(--sun-light), var(--sun) 60%, var(--sun-edge)); }
  .brand__name { font-weight: 700; font-size: 62px; letter-spacing: -1px; color: var(--leaf); line-height: 1; }

  .band { position: absolute; left: 0; right: 0; top: 12px; height: 48px;
    background: linear-gradient(to bottom, var(--band-top), var(--band-bottom));
    text-align: center; color: var(--leaf); padding-top: 7px; }
  .band__name { font-weight: 700; font-size: 15px; line-height: 18px; }
  .band__title { font-weight: 700; font-style: italic; font-size: 13px; line-height: 16px; }

  .corner-dot { position: absolute; left: -28px; bottom: -30px; width: 150px; height: 150px; border-radius: 50%;
    background: radial-gradient(circle at 60% 40%, var(--sun-light), var(--sun) 55%, var(--sun-edge)); }

  .contact { position: absolute; left: 157px; top: 99px; list-style: none;
    color: var(--leaf); font-size: 12px; line-height: 18px; }
</style>
</head>
<body>

  <section class="card card--back" style="top:27px"><div class="brand"><span class="brand__dot"></span><span class="brand__name">BrightNest</span></div></section>
  <section class="card card--front" style="top:27px">
    <div class="band"><p class="band__name">(name goes here)</p><p class="band__title">position</p></div>
    <span class="corner-dot"></span>
    <ul class="contact"><li>Mobile: 555.0142881</li><li>Office: 555.0193370</li><li>E-mail: hello@brightnest.com</li><li>Address: PO Box 10482, City, USA</li><li>ABN: #########</li></ul>
  </section>

  <section class="card card--back" style="top:261px"><div class="brand"><span class="brand__dot"></span><span class="brand__name">BrightNest</span></div></section>
  <section class="card card--front" style="top:261px">
    <div class="band"><p class="band__name">(name goes here)</p><p class="band__title">position</p></div>
    <span class="corner-dot"></span>
    <ul class="contact"><li>Mobile: 555.0142881</li><li>Office: 555.0193370</li><li>E-mail: hello@brightnest.com</li><li>Address: PO Box 10482, City, USA</li><li>ABN: #########</li></ul>
  </section>

  <section class="card card--back" style="top:494px"><div class="brand"><span class="brand__dot"></span><span class="brand__name">BrightNest</span></div></section>
  <section class="card card--front" style="top:494px">
    <div class="band"><p class="band__name">(name goes here)</p><p class="band__title">position</p></div>
    <span class="corner-dot"></span>
    <ul class="contact"><li>Mobile: 555.0142881</li><li>Office: 555.0193370</li><li>E-mail: hello@brightnest.com</li><li>Address: PO Box 10482, City, USA</li><li>ABN: #########</li></ul>
  </section>

  <section class="card card--back" style="top:728px"><div class="brand"><span class="brand__dot"></span><span class="brand__name">BrightNest</span></div></section>
  <section class="card card--front" style="top:728px">
    <div class="band"><p class="band__name">(name goes here)</p><p class="band__title">position</p></div>
    <span class="corner-dot"></span>
    <ul class="contact"><li>Mobile: 555.0142881</li><li>Office: 555.0193370</li><li>E-mail: hello@brightnest.com</li><li>Address: PO Box 10482, City, USA</li><li>ABN: #########</li></ul>
  </section>

  <section class="card card--back" style="top:961px"><div class="brand"><span class="brand__dot"></span><span class="brand__name">BrightNest</span></div></section>
  <section class="card card--front" style="top:961px">
    <div class="band"><p class="band__name">(name goes here)</p><p class="band__title">position</p></div>
    <span class="corner-dot"></span>
    <ul class="contact"><li>Mobile: 555.0142881</li><li>Office: 555.0193370</li><li>E-mail: hello@brightnest.com</li><li>Address: PO Box 10482, City, USA</li><li>ABN: #########</li></ul>
  </section>

</body>
</html>
```